Professional & Modern Technology Business Card

We need a business card for our software/technology firm. Our services include Program/Project Management, Project Controls and Enterprise Analytics. Our clients are usually in the Aviation, Public Works, Transportation and Electric & Water Utility industries. We serve both public and private clients. Would like a very professional, conservative but somewhat modern design. Design, Develop, Deploy is the corporate tagline. We have two offices. The headquarters is in Atlanta, GA and a satellite office In Savannah, GA. Corporate Logo Attached.
Looking to do website and corporate brochure after the successful completion of this project. Would like to begin a working relationship with best designers.
Tagline: Design, Develop, Deploy
Website: www.quelvanesystems.example
My Name: Marla Dunstead
My Title: CEO
Email: mdunstead@quelvanesystems.example
Atlanta Address:
87 Corliss Avenue, #2291
Atlanta, GA 30301
Office: 404.555.0182
Fax: 404.555.0147
Mobile: 404.555.0163
Savannah Address:
350 West Harrow Bend Road
Suite 720
Savannah, GA 31401
Office: 912.555.0139
Fax: 404.555.0147
Mobile: 404.555.0163
Updates
Please include the email address in your designs: mdunstead@quelvanesystems.example.
I appreciate everyone's design efforts. Just a few notes:
1. Please remove the mobile number from the cards
2. The backs of the cards can be utilized for writing notes. Make sure your design on the back of the card is conducive to clearly adding writing if needed.
3. No black backgrounds please
4. Only use the corporate logo on the front of the card. You can use portions of the logo design, but not the logo in totality.
Thank You
Industry/Entity Type
Conservative
Look and feel
Each slider illustrates characteristics of the customer's brand and the style your logo design should communicate.

```html
<!DOCTYPE html>
<html lang="en">
<head>
<meta charset="utf-8">
<title>Quelvane Systems, Inc. — Business Card</title>
<link rel="stylesheet" href="https://fonts.googleapis.com/css2?family=Arimo:wght@400;700&family=Michroma&display=swap">
<style>
  :root {
    --page: #ffffff;
    --card-white: #ffffff;
    --card-light: #f3f3f1;
    --card-light-deep: #e6e6e3;
    --brand-yellow: #f2d21a;
    --brand-gold: #b89a00;
    --brand-green: #8cc63f;
    --text-dark: #1a1a1a;
    --text-body: #2c2c2c;
    --text-muted: #555555;
    --divider: #b5b5b5;
  }
  * { box-sizing: border-box; margin: 0; padding: 0; }
  html, body {
    width: 1200px; height: 900px; overflow: hidden;
    background: var(--page);
    font-family: "Arimo", Arial, sans-serif;
  }
  .stage {
    position: relative; width: 1200px; height: 900px;
    display: flex; align-items: center; justify-content: center; gap: 40px;
  }
  .card {
    position: relative; width: 540px; height: 309px;
    border-radius: 22px; overflow: hidden;
    box-shadow: 0 12px 26px rgba(0,0,0,0.16), 0 0 0 1px rgba(0,0,0,0.05);
  }

  /* ---------- Front card ---------- */
  .card--front { background: var(--card-white); }
  .front__header { position: relative; height: 140px; }
  .brand {
    position: absolute; left: 26px; top: 34px;
    display: flex; align-items: center; gap: 12px;
  }
  .brand__dot {
    width: 46px; height: 46px; border-radius: 50%;
    background: var(--brand-yellow);
  }
  .brand__name {
    font-weight: 700; font-size: 27px; line-height: 1.05;
    color: var(--text-dark); letter-spacing: -0.5px;
  }
  .person {
    position: absolute; right: 30px; top: 26px; text-align: center;
  }
  .person__name { font-weight: 700; font-size: 17px; color: var(--text-dark); }
  .person__title { font-size: 10px; color: var(--text-muted); margin-top: 3px; }

  .tagline-band {
    height: 16px; background: var(--brand-yellow);
    display: flex; align-items: center; justify-content: flex-end;
    padding-right: 24px;
  }
  .tagline {
    font-family: "Michroma", "Arimo", sans-serif;
    font-size: 9px; letter-spacing: 5px; color: var(--text-dark);
    word-spacing: 26px; text-transform: uppercase;
  }

  .front__body {
    height: 153px;
    background: linear-gradient(180deg, var(--card-light) 0%, var(--card-light-deep) 100%);
    color: var(--text-body); padding: 14px 22px 0 22px;
    display: grid; grid-template-columns: 1fr 1px 1.15fr; grid-template-rows: auto 1fr;
    column-gap: 16px;
    font-size: 12px; line-height: 1.5;
  }
  .contact-email { grid-column: 1 / 4; display: flex; align-items: center; gap: 6px; margin-bottom: 10px; }
  .office { display: flex; flex-direction: column; }
  .office__divider { background: var(--divider); margin: 0 0 26px; }
  .line { display: flex; align-items: center; gap: 6px; white-space: nowrap; }
  .line--indent { padding-left: 17px; }
  .icon { width: 11px; height: 11px; flex: none; fill: var(--brand-gold); }

  /* ---------- Back card (notes side) ---------- */
  .card--back { background: var(--card-white); }
  .back__accent {
    position: absolute; left: 0; right: 0; bottom: 0; height: 16px;
    background: var(--brand-yellow);
  }
  .website {
    position: absolute; left: 0; right: 0; bottom: 34px; text-align: center;
    font-size: 14px; letter-spacing: 5px; color: var(--text-muted);
  }
</style>
</head>
<body>
<main class="stage">

  <section class="card card--front" aria-label="Business card front">
    <header class="front__header">
      <div class="brand">
        <span class="brand__dot"></span>
        <span class="brand__name">Quelvane<br>Systems, Inc.</span>
      </div>
      <div class="person">
        <p class="person__name">Marla Dunstead</p>
        <p class="person__title">CEO</p>
      </div>
    </header>

    <div class="tagline-band">
      <p class="tagline">Design, Develop, Deploy</p>
    </div>

    <div class="front__body">
      <p class="contact-email">
        <svg class="icon" viewBox="0 0 12 12"><path d="M0 2h12v8H0z"/><path d="M1 3l5 4 5-4" fill="none" stroke="#ffffff" stroke-width="0.9"/></svg>
        mdunstead@quelvanesystems.example
      </p>

      <div class="office office--primary">
        <p class="line"><svg class="icon" viewBox="0 0 12 12"><path d="M6 0L0 6h2v6h3V8h2v4h3V6h2z"/></svg>87 Corliss Avenue, #2291</p>
        <p class="line line--indent">Atlanta, GA 30301</p>
        <p class="line"><svg class="icon" viewBox="0 0 12 12"><path d="M2 0l3 3-1.5 1.5a8 8 0 0 0 4 4L9 7l3 3-2 2C4 12 0 8 0 2z"/></svg>Office: 404.555.0182</p>
        <p class="line"><svg class="icon" viewBox="0 0 12 12"><path d="M3 0h6v3H3z M1 4h10v6H1z M3 10h6v2H3z"/></svg>Fax: 404.555.0147</p>
      </div>

      <span class="office__divider"></span>

      <div class="office office--secondary">
        <p class="line"><svg class="icon" viewBox="0 0 12 12"><path d="M6 0L0 6h2v6h3V8h2v4h3V6h2z"/></svg>350 West Harrow Bend Road</p>
        <p class="line line--indent">Suite 720, Savannah, GA 31401</p>
        <p class="line"><svg class="icon" viewBox="0 0 12 12"><path d="M2 0l3 3-1.5 1.5a8 8 0 0 0 4 4L9 7l3 3-2 2C4 12 0 8 0 2z"/></svg>Office: 912.555.0139</p>
        <p class="line"><svg class="icon" viewBox="0 0 12 12"><path d="M3 0h6v3H3z M1 4h10v6H1z M3 10h6v2H3z"/></svg>Fax: 404.555.0147</p>
      </div>
    </div>
  </section>

  <section class="card card--back" aria-label="Business card back, open space for notes">
    <p class="website">www.quelvanesystems.example</p>
    <span class="back__accent"></span>
  </section>

</main>
</body>
</html>
```